Food and Beverage Business Cards

We need business cards with logo designs for a consultant in the food and beverage industry. We specialize in helping restaurants fix operational and management problems.
Specific areas of expertise include:
-Steps of service
-Staff management tools
-Standard operating procedures
-Profit and loss management
-Inventory
-Point of sales
-Bar Menu
-Mystery shopper service
-Handling and managing suppliers

Target Market(s)

Restaurant and bar owners and managers

Industry/Entity Type

Business

Contact Information for Business Card

Mathieu Delorme
K&T Consulting
phone: 15027390618
mathkt@brindlemail.net

Font styles to use
Other font styles liked:
• Check out the screen shot font idea

Colors

Designer to choose colors to be used in the design.

Requirements
Must have
• Must include QR code (See attachment)
• Logo should reflect our specific focus on the drinks side of the industry.
• Areas of Expertise:
• -Service Steps
• -Staff management tools
• -S.O.P
• -P&L Management
• -Inventory
• -P.O.S
• -Bar Menu
• -Mystery Shopper Service
• -Handling and Managing Suppliers

```html
<!DOCTYPE html>
<html lang="en">
<head>
<meta charset="utf-8">
<title>K&amp;T Consulting Business Cards</title>
<link rel="stylesheet" href="https://fonts.googleapis.com/css2?family=Tinos&family=Roboto:wght@400;700&display=swap">
<style>
  :root {
    --canvas: #e9e6e1;
    --card-light: #f7f7f5;
    --card-dark: #151515;
    --ink: #1c1c1c;
    --ink-soft: #555555;
    --rule: #9a9a9a;
    --paper-text: #f2f2f2;
    --badge: #dcdcdc;
  }
  * { box-sizing: border-box; margin: 0; padding: 0; }
  html, body { width: 1200px; height: 886px; overflow: hidden; }
  body {
    background: var(--canvas);
    position: relative;
    font-family: "Tinos", serif;
  }
  .card {
    position: absolute;
    top: 288px;
    width: 540px;
    height: 309px;
    border-radius: 4px;
    box-shadow: 0 6px 18px rgba(0,0,0,0.18);
    overflow: hidden;
  }
  /* Front */
  .card-front { left: 40px; background: var(--card-light); color: var(--ink); }
  .front-brand {
    position: absolute; left: 0; top: 0; width: 255px; height: 100%;
    display: flex; align-items: center; justify-content: center;
  }
  .brand-name {
    font-family: "Tinos", serif;
    font-weight: 400;
    font-size: 44px;
    letter-spacing: 1px;
    color: var(--ink);
  }
  .front-divider {
    position: absolute; left: 268px; top: 40px; width: 1px; height: 229px;
    background: var(--rule);
  }
  .front-details { position: absolute; left: 292px; top: 92px; }
  .person-name { font-size: 21px; letter-spacing: 0.5px; text-transform: uppercase; }
  .person-role {
    font-size: 12px; color: var(--ink-soft); text-transform: uppercase;
    letter-spacing: 0.8px; margin-top: 4px;
  }
  .contact-list { list-style: none; margin-top: 22px; }
  .contact-list li {
    display: flex; align-items: center; gap: 8px;
    font-size: 12.5px; line-height: 22px; color: var(--ink);
  }
  .contact-list svg { width: 11px; height: 11px; flex: none; }
  .front-tab {
    position: absolute; left: 0; bottom: 0; width: 120px; height: 8px;
    background: var(--card-dark); border-radius: 0 6px 0 0;
  }
  /* Back */
  .card-back { left: 620px; background: var(--card-dark); color: var(--paper-text); }
  .expertise {
    position: absolute; left: 30px; top: 40px; width: 240px;
    font-family: "Roboto", sans-serif;
  }
  .expertise-title { font-size: 15px; font-weight: 700; margin-bottom: 12px; }
  .expertise-list { list-style: none; font-size: 11.5px; line-height: 20px; font-weight: 400; }
  .back-brand {
    position: absolute; right: 40px; top: 110px;
  }
  .back-brand .brand-name { color: var(--paper-text); font-size: 46px; }
  .badges { position: absolute; right: 22px; bottom: 22px; display: flex; gap: 10px; }
  .badge { width: 40px; height: 40px; border-radius: 50%; background: var(--badge); }
</style>
</head>
<body>
  <section class="card card-front" aria-label="Business card front">
    <div class="front-brand"><span class="brand-name">K&amp;T Atlanta</span></div>
    <div class="front-divider"></div>
    <div class="front-details">
      <h1 class="person-name">Mathieu Delorme</h1>
      <p class="person-role">K&amp;T Consulting</p>
      <ul class="contact-list">
        <li>
          <svg viewBox="0 0 12 12" aria-hidden="true"><path d="M2.5 1 L4.5 1 L5.3 3.6 L4 4.6 Q5 7 7.4 8 L8.4 6.7 L11 7.5 L11 9.5 Q10.5 11 9 11 Q1 10 1 2.5 Q1 1 2.5 1 Z" fill="currentColor"/></svg>
          15027390618
        </li>
        <li>
          <svg viewBox="0 0 12 12" aria-hidden="true"><rect x="0.5" y="2" width="11" height="8" rx="1" fill="currentColor"/><path d="M1 2.8 L6 6.6 L11 2.8" stroke="#f7f7f5" stroke-width="1" fill="none"/></svg>
          mathkt@brindlemail.net
        </li>
        <li>
          <svg viewBox="0 0 12 12" aria-hidden="true"><circle cx="6" cy="6" r="5.5" fill="currentColor"/><path d="M0.8 6 H11.2 M6 0.6 Q3 6 6 11.4 M6 0.6 Q9 6 6 11.4" stroke="#f7f7f5" stroke-width="0.8" fill="none"/></svg>
          www.ktatlanta-bar.com
        </li>
      </ul>
    </div>
    <div class="front-tab"></div>
  </section>

  <section class="card card-back" aria-label="Business card back">
    <div class="expertise">
      <h2 class="expertise-title">Areas of Expertise</h2>
      <ul class="expertise-list">
        <li>Service Steps | Staff Management Tools</li>
        <li>S.O.P | P&amp;L Management</li>
        <li>Inventory | P.O.S | Bar Menu</li>
        <li>Mystery Shopper Service</li>
        <li>Handling &amp; Managing Suppliers</li>
      </ul>
    </div>
    <div class="back-brand"><span class="brand-name">K&amp;T Atlanta</span></div>
    <div class="badges">
      <span class="badge"></span>
      <span class="badge"></span>
    </div>
  </section>
</body>
</html>
```